Can you make FairlyNeat look better than average? We need business cards and a logo refresh :-)

REVISED BRIEF

PRIORITY

VECTOR LOGO

Create a vector version of our existing logo. The logo must not change from its current design, weight or font.

Deliverables

- Logo in blue (#2540BB)
- Logo in white (#FFFFFF)
- Logo in grey (#36454F)
- All logos on transparent background
- All logos in PNG & SVG formats. (SVG must NOT distort stroke width when resized)

BRAND MARK

Create a brand mark for use with the logo. This should be possible to used with the logo and on its own as a stand alone graphical device that represents the FairlyNeat brand.

https://pagewrightly.com/resources/glossary/what-is-a-brand-mark

Deliverables

- Brand Mark in blue (#2540BB)
- Brand Mark in white (#FFFFFF)
- Brand Mark in grey (#36454F)
- Brand Mark on transparent background
- Brand Mark in PNG & SVG formats. (SVG must NOT distort stroke width when resized)
- Logo combined with Brand Mark (colours and formats)
.

Business Card Layout

Create 2 layouts with the following details:-

Marcus Thorne
Co-Founder & Chief Product Officer

marcus@fairlyneat.nz
www.fairlyneat.nz
0279183640

Duncan Wells
Founder & CEO

hello@fairlyneat.nz
www.fairlyneat.nz
021 468 9271

DESIGN CONSIDERATIONS

Create versions with ‘Shaping Labels With Heart’ tag line incorporated within the design and without (maintain separation of logo from tag line)

- Create a version with and without the brand mark
- Keep it clean and simple but elevate the design with subtle design effects
- Consider use of raised spot gloss colour (this can be white on white for subtle or blue on blue or blue on white)
- Consider use of spot gloss colour (this can be white on white for subtle or blue on blue or blue on white)
- Consider use of letterpress indentation
- Ensure contact details are legible, use sans-serif font

PREVIOUS BRIEF

We need a business card design for our business FairlyNeat. We are a purpose driven brand and media agency that helps brands and charities plan and buy traditional media campaigns (TV, Radio, Print, Outdoor etc). We give a significant amount of the media booking fees we receive from media vendors to charity in the name of our clients. https://www.linkedin.com/posts/wearefairlyneat_giveback-fairlyneat-shapinglabelswithheart-activity-7000000000000000000-Xqzt

Our strapline is 'Shaping Labels With Heart'.

We want to keep our logo design as it is but it does need tightening up and made into a proper vector image as it's been created from a font.

Our brand colour is #2540BB and we need to keep this.

Our brand is professional but human, warm and engaging and doesn't take itself too seriously.

Things We Need
- vectorisation and tidying up of existing logo
- We'd like you to think about how we can incorporate a brand mark with the logo to add another dimension to our brand
- business card layout and design
- we'll be using printzo.com to print the cards so please take a look at the options they have (spot gloss, foil, letterpress, square cards and even the backs of the cards can have a different design on every single card!
- potential opportunity for different famous quotes on the back or imagery or slight design differences
- we'd be open to the use of an emoji or emojiis as the brandmark or to be incorporated into the card designs
- we can have as many different design batches as we like for the backs of the cards

https://www.printzo.com/au/business-cards

We want to make an impact, we want to be seen as professional but fun, we want to be different.

Here's a press release of what we're about.

https://adwirenews.co.nz/movings-shakings/fairlyneat-welcomes-marcus-thorne-as-co-founder/

Be bold, be different, there is no such thing as a bad idea. We're open to anything so please bring your best ideas and have fun with it! Go crazy if you like!
____________
Marcus Thorne
marcus@fairlyneat.nz
0279183640

Duncan Wells
Founder & CEO
hello@fairlyneat.nz
021 468 9271

Shaping Labels With Heart

________

These are the only details we MUST have on the cards, the rest is up to you. Just make sure you use all of your creativity but don't feel the need to crowd the card with too much, let it breathe as well.

In terms of font for the details, we'll leave that up to you, just ensure it's legible. Oh and please don't take any design inspiration from our website - that will be changing!

Please don't let the design and layout look cheap and tacky though. It needs to still feel premium but personable.

Thanks

Marcus
Updates

Many designs are changing the logo and this was NOT in the brief. We need a brand mark to complement the logo. We need to see the logo with and without the brand mark. We need to see the business card with both logo + brand mark and logo on its own We need to see the business card with and without the tagline 'Shaping Labels With Heart'

Industry/Entity Type

purpose driven Brand & Media Agency

Contact Information for Business Card

Shaping Labels With Heart
Marcus Thorne, Co-Founder & Chief Product Officer, marcus@fairlyneat.nz fairlyneet.nz, 0279 183 640

Duncan Wells, Founder & CEO hello@fairlyneat.nz, fairlyneet.nz, 021 468 9271

Font styles to use
Serif
Sans Serif

Colors
0054AA
0677BA
7BADD7
CADEEF
E8F1F8

Requirements
Must have
• brand mark, vector version of existing logo, Shaping Labels With Heart tagline, existing logo traced and vectorised. Must fully explore the design options from printzo.com that can enhance the overall card design
Nice to have
• brandmark to help elevate the logo, maybe incorporate some other design elements into the card like lines, or grids.
Should not have
• A cheap look and feel

```html
<!DOCTYPE html>
<html lang="en">
<head>
<meta charset="utf-8">
<title>FairlyNeat — Business Cards</title>
<link rel="stylesheet" href="https://fonts.googleapis.com/css2?family=Open+Sans:wght@400;600;700&display=swap">
<style>
  :root {
    --backdrop: #1f1f1f;
    --brand-blue: #2f3296;
    --brand-blue-deep: #272a85;
    --brand-blue-soft: #3a4bb0;
    --paper-white: #ffffff;
    --card-shadow: rgba(0, 0, 0, 0.45);
  }

  * { box-sizing: border-box; margin: 0; padding: 0; }

  html, body {
    width: 1200px;
    height: 780px;
    overflow: hidden;
    background: var(--backdrop);
    font-family: "Open Sans", Arial, sans-serif;
  }

  .canvas {
    position: relative;
    width: 1200px;
    height: 780px;
  }

  .card {
    position: absolute;
    background: var(--brand-blue);
    box-shadow: 0 18px 40px var(--card-shadow);
    overflow: hidden;
    color: var(--paper-white);
  }

  /* Front: portrait card */
  .card--front {
    left: 150px;
    top: 110px;
    width: 320px;
    height: 560px;
  }

  .front-header {
    position: absolute;
    left: 0;
    top: 0;
    width: 100%;
    height: 92px;
    background: var(--paper-white);
    display: flex;
    flex-direction: column;
    justify-content: center;
    padding: 0 24px;
  }

  .name-lockup {
    display: flex;
    align-items: center;
    gap: 10px;
  }

  .name-dot {
    width: 12px;
    height: 12px;
    border-radius: 50%;
    flex: none;
  }

  .company-name {
    font-weight: 600;
    line-height: 1;
    letter-spacing: 0;
  }

  .tagline {
    font-weight: 400;
    line-height: 1.2;
  }

  .front-header .name-dot { background: var(--brand-blue); }

  .front-header .company-name {
    color: var(--brand-blue);
    font-size: 30px;
  }

  .front-header .tagline {
    color: var(--brand-blue);
    font-size: 12px;
    margin-top: 6px;
    padding-left: 22px;
  }

  .contact-block {
    position: absolute;
    left: 300px;
    top: 205px;
    width: 330px;
    transform-origin: top left;
    transform: rotate(90deg);
    text-align: right;
  }

  .contact-name {
    font-size: 27px;
    font-weight: 700;
    line-height: 1.15;
  }

  .contact-role {
    font-size: 15px;
    font-weight: 400;
    line-height: 1.3;
    margin-bottom: 12px;
  }

  .contact-line {
    display: flex;
    justify-content: flex-end;
    align-items: center;
    gap: 7px;
    font-size: 14px;
    line-height: 1.45;
  }

  .contact-icon {
    width: 13px;
    height: 13px;
    flex: none;
  }

  .edge-tab {
    position: absolute;
    left: 266px;
    bottom: 0;
    width: 36px;
    height: 20px;
    background: var(--paper-white);
  }

  /* Back: landscape card */
  .card--back {
    left: 540px;
    top: 200px;
    width: 560px;
    height: 320px;
  }

  .back-pattern {
    position: absolute;
    inset: 0;
    background: linear-gradient(90deg, var(--brand-blue-deep) 0%, var(--brand-blue) 50%, var(--brand-blue-soft) 100%);
  }

  .back-lockup {
    position: absolute;
    left: 50%;
    top: 50%;
    transform: translate(-50%, -50%);
  }

  .back-lockup .name-lockup { gap: 14px; }

  .back-lockup .name-dot {
    width: 18px;
    height: 18px;
    background: var(--paper-white);
  }

  .back-lockup .company-name {
    color: var(--paper-white);
    font-size: 54px;
  }

  .back-lockup .tagline {
    color: var(--paper-white);
    font-size: 17px;
    margin-top: 10px;
    padding-left: 32px;
  }
</style>
</head>
<body>
<main class="canvas">

  <section class="card card--front" aria-label="Business card front">
    <header class="front-header">
      <div class="name-lockup">
        <span class="name-dot"></span>
        <span class="company-name">FairlyNeat</span>
      </div>
      <div class="tagline">Shaping Labels With Heart</div>
    </header>

    <div class="contact-block">
      <p class="contact-name">Duncan Wells</p>
      <p class="contact-role">Founder &amp; CEO</p>
      <p class="contact-line">
        <span>021 468 9271</span>
        <svg class="contact-icon" viewBox="0 0 16 16" aria-hidden="true">
          <path fill="#fff" d="M4.2 1.5 6 4.6c.2.4.1.8-.2 1.1L4.8 6.6a8.6 8.6 0 0 0 4.6 4.6l.9-1c.3-.3.7-.4 1.1-.2l3.1 1.8c.4.2.5.7.3 1.1l-.9 1.5c-.3.5-.9.8-1.5.7C6.6 14.4 1.6 9.4 0.9 3.6c-.1-.6.2-1.2.7-1.5L3.1 1.2c.4-.2.9-.1 1.1.3z"/>
        </svg>
      </p>
      <p class="contact-line">
        <span>www.fairlyneat.nz</span>
        <svg class="contact-icon" viewBox="0 0 16 16" aria-hidden="true">
          <circle cx="8" cy="8" r="7" fill="none" stroke="#fff" stroke-width="1.4"/>
          <ellipse cx="8" cy="8" rx="3" ry="7" fill="none" stroke="#fff" stroke-width="1.2"/>
          <path d="M1 8h14M2.2 4.5h11.6M2.2 11.5h11.6" stroke="#fff" stroke-width="1.1"/>
        </svg>
      </p>
      <p class="contact-line">
        <span>hello@fairlyneat.nz</span>
        <svg class="contact-icon" viewBox="0 0 16 16" aria-hidden="true">
          <rect x="1" y="3.5" width="14" height="10" rx="1" fill="none" stroke="#fff" stroke-width="1.4"/>
          <path d="M1.5 4.2 8 9.2l6.5-5" fill="none" stroke="#fff" stroke-width="1.4"/>
        </svg>
      </p>
    </div>

    <div class="edge-tab"></div>
  </section>

  <section class="card card--back" aria-label="Business card back">
    <div class="back-pattern" role="img" aria-label="Faint repeated company name pattern in tonal blues"></div>
    <div class="back-lockup">
      <div class="name-lockup">
        <span class="name-dot"></span>
        <span class="company-name">FairlyNeat</span>
      </div>
      <div class="tagline">Shaping Labels With Heart</div>
    </div>
  </section>

</main>
</body>
</html>
```